Postcard Design

I am an attorney in Pittsburgh. Here and across country, companies are sending data with names, address and new criminal charges for people. This has resulted in some people getting 12 or more of these letters. I want to do a postcard because one does not need to open a postcard. I also want to be delicate since there is no sealed envelope. I want to throw in other matters other than criminal so it does not look like the person is necessarily charged with a crime.
At top would be "Law Office of Dennis K. Varholtz"
Then:
Need an Attorney?
Attorney Dennis K. Varholtz has 25 Years of Experience
Free Consultation - Affordable Fees - Credit Cards Accepted
-All Criminal Matters
-Most Civil Matters
-DUI / Traffic Citations / License Restoration
412-555-0187
www.harbordefensecounsel.example
www.dkvcounsel.example

My CTQ ranking is A+ but I am not sure they give a logo with the rating. I have all my logos at www.harbordefensecounsel.example The purpose of the two websites is these are postcards. I want no one to think oh this person is charged with a crime.

```html
<!DOCTYPE html>
<html lang="en">
<head>
<meta charset="utf-8">
<title>Law Office of Dennis K. Varholtz – Postcard</title>
<link rel="stylesheet" href="https://fonts.googleapis.com/css2?family=Cormorant+Garamond:wght@600;700&family=Open+Sans:wght@400;600;700&family=Roboto+Condensed:wght@700&display=swap">
<style>
  :root {
    --navy: #1c2b4f;
    --teal: #1f9bb4;
    --teal-dark: #17819a;
    --ink: #2a2d33;
    --blue-text: #1d5a9a;
    --stage: #ece9e4;
    --card-front-a: #f3efe6;
    --card-front-b: #c9cfd6;
    --photo-panel: #7d9fbe;
    --grey-box: #5b5d62;
    --light-box: #d3d5d8;
    --rule: #1c2b4f;
  }
  * { box-sizing: border-box; margin: 0; padding: 0; }
  html, body { width: 1200px; height: 442px; overflow: hidden; }
  body { background: var(--stage); position: relative; font-family: "Open Sans", Arial, sans-serif; color: var(--ink); }

  .card { position: absolute; top: 45px; width: 546px; height: 352px; overflow: hidden; box-shadow: 0 2px 6px rgba(0,0,0,.18); }
  .card--front { left: 37px; }
  .card--back { left: 612px; width: 545px; background: #fff; }

  .front-backdrop { position: absolute; inset: 0; background: linear-gradient(100deg, var(--card-front-a) 0%, #e4e2de 45%, var(--card-front-b) 100%); }

  .brand { position: absolute; text-align: center; }
  .brand__mark { display: inline-flex; align-items: center; gap: 6px; font-family: "Cormorant Garamond", Georgia, serif; font-weight: 700; font-size: 20px; color: var(--navy); }
  .brand__square { width: 26px; height: 26px; background: var(--navy); }
  .brand__pre { display: flex; align-items: center; justify-content: center; gap: 8px; margin-top: 10px; font-family: "Cormorant Garamond", Georgia, serif; font-weight: 700; font-variant: small-caps; font-size: 13px; letter-spacing: 1px; color: var(--navy); }
  .brand__pre::before, .brand__pre::after { content: ""; width: 46px; height: 2px; background: var(--rule); }
  .brand__name { font-family: "Cormorant Garamond", Georgia, serif; font-weight: 700; font-variant: small-caps; font-size: 22px; letter-spacing: .5px; color: var(--navy); line-height: 1; }

  .front .brand { left: 0; width: 306px; top: 17px; }

  .band { position: absolute; left: 0; right: 0; top: 103px; height: 31px; background: linear-gradient(90deg, var(--teal-dark), var(--teal) 50%, var(--teal-dark)); }
  .band__title { position: absolute; left: 0; width: 306px; top: 0; line-height: 31px; text-align: center; font-family: "Cormorant Garamond", Georgia, serif; font-weight: 700; font-size: 22px; color: #fff; }

  .experience { position: absolute; left: 0; width: 306px; top: 139px; text-align: center; font-weight: 700; font-size: 15px; line-height: 17px; color: var(--ink); }

  .practice { position: absolute; left: 19px; top: 185px; }
  .practice__head { font-family: "Roboto Condensed", Arial Narrow, sans-serif; font-weight: 700; font-size: 16px; color: var(--blue-text); letter-spacing: .3px; }
  .practice__list { list-style: none; margin-top: 1px; }
  .practice__list li { font-weight: 700; font-size: 12.5px; line-height: 15.5px; color: var(--ink); }
  .practice__list li::before { content: "•"; color: var(--blue-text); margin-right: 4px; }

  .photo-panel { position: absolute; left: 306px; top: 23px; width: 226px; height: 254px; border-radius: 12px; background: var(--photo-panel); box-shadow: 0 3px 8px rgba(0,0,0,.25); }
  .photo-panel__photo { position: absolute; left: 18px; top: 22px; width: 190px; height: 190px; border-radius: 50%; background: radial-gradient(circle at 50% 45%, #8a97a5 0%, #4c5d72 60%, #1e3a63 100%); box-shadow: 0 0 0 5px #2f5f93; }

  .badges { position: absolute; left: 28px; top: 283px; display: flex; align-items: center; gap: 18px; }
  .badge--round { width: 50px; height: 50px; border-radius: 50%; background: #2d3a66; }
  .badge--gold { background: #b59a4a; }
  .badge--tall { width: 26px; height: 44px; background: #2c5e8f; }

  .contact { position: absolute; left: 222px; top: 270px; width: 180px; white-space: nowrap; }
  .contact__phone { display: flex; align-items: center; gap: 4px; font-weight: 700; font-size: 13px; color: var(--blue-text); }
  .contact__web { font-size: 10px; line-height: 14px; letter-spacing: -.1px; color: var(--ink); }

  .offer { position: absolute; left: 407px; top: 286px; width: 110px; text-align: center; }
  .offer span { display: block; height: 16px; line-height: 16px; white-space: nowrap; }
  .offer__free { background: var(--grey-box); color: #fff; font-family: "Roboto Condensed", Arial Narrow, sans-serif; font-weight: 700; font-size: 12px; }
  .offer__fees { background: var(--teal); color: #fff; font-weight: 700; font-size: 10.5px; }
  .offer__cards { background: var(--light-box); color: var(--ink); font-size: 9.5px; }

  .back-strip { position: absolute; left: 0; right: 0; top: 8px; height: 8px; background: linear-gradient(90deg, #dfe6f2, #7e95bf 50%, #2b4f7f); }
  .back-photo { position: absolute; left: 0; top: 16px; width: 171px; height: 288px; background: linear-gradient(180deg, #2a60a8 0%, #7fa7d4 45%, #8b8d8e 68%, #5d6f78 82%, #3c5560 100%); }
  .stamp { position: absolute; left: 476px; top: 23px; width: 52px; height: 52px; border: 1.5px dashed #9da2a8; }
  .back .brand { left: 171px; width: 215px; top: 18px; }
  .address { position: absolute; left: 224px; top: 101px; font-size: 10.5px; line-height: 14px; color: var(--ink); font-style: normal; }
  .back-contact { position: absolute; left: 204px; top: 267px; font-size: 10.5px; line-height: 14px; color: var(--ink); white-space: nowrap; }
  .back-contact__phone { display: flex; align-items: center; gap: 4px; }
  .back-contact__fax { padding-left: 22px; }
</style>
</head>
<body>

<section class="card card--front front">
  <div class="front-backdrop" role="img" aria-label="Faded photograph of a judge's gavel on a soft grey background"></div>

  <div class="brand">
    <div class="brand__mark"><span class="brand__square"></span>DKV</div>
    <div class="brand__pre">Law Office of</div>
    <div class="brand__name">Dennis K. Varholtz</div>
  </div>

  <div class="band"><h1 class="band__title">Need an Attorney?</h1></div>

  <p class="experience">Attorney Dennis K. Varholtz<br>has 25 Years of Experience</p>

  <div class="practice">
    <h2 class="practice__head">ALL CRIMINAL MATTERS</h2>
    <ul class="practice__list">
      <li>Most Civil Matters</li>
      <li>DUI</li>
      <li>Traffic Citations</li>
      <li>License Restoration</li>
    </ul>
  </div>

  <div class="photo-panel">
    <div class="photo-panel__photo" role="img" aria-label="Photograph of a police officer writing a ticket in a patrol car"></div>
  </div>

  <div class="badges">
    <span class="badge badge--round"></span>
    <span class="badge badge--round badge--gold"></span>
    <span class="badge badge--tall"></span>
  </div>

  <div class="contact">
    <p class="contact__phone">
      <svg width="12" height="12" viewBox="0 0 24 24" aria-hidden="true"><circle cx="12" cy="12" r="11" fill="none" stroke="currentColor" stroke-width="2"/><path d="M8 6c1 0 2 2 2 3s-1 1-1 2 2 3 3 4 1-1 2-1 3 1 3 2-1 2-2 2C10 18 6 14 6 8c0-1 1-2 2-2z" fill="currentColor"/></svg>
      412.555.0187
    </p>
    <p class="contact__web">www.harbordefensecounsel.example</p>
    <p class="contact__web">www.dkvcounsel.example</p>
  </div>

  <div class="offer">
    <span class="offer__free">FREE CONSULTATION</span>
    <span class="offer__fees">Affordable Fees</span>
    <span class="offer__cards">Credit Cards Accepted</span>
  </div>
</section>

<section class="card card--back back">
  <div class="back-strip"></div>
  <div class="back-photo" role="img" aria-label="Photograph of a city skyline across a river"></div>
  <div class="stamp"></div>

  <div class="brand">
    <div class="brand__mark"><span class="brand__square"></span>DKV</div>
    <div class="brand__pre">Law Office of</div>
    <div class="brand__name">Dennis K. Varholtz</div>
  </div>

  <address class="address">
    1800 Counsel Tower<br>
    215 Harbor Street<br>
    Pittsburgh, PA 15219
  </address>

  <div class="back-contact">
    <p class="back-contact__phone">
      <svg width="12" height="12" viewBox="0 0 24 24" aria-hidden="true"><circle cx="12" cy="12" r="11" fill="none" stroke="currentColor" stroke-width="2"/><path d="M8 6c1 0 2 2 2 3s-1 1-1 2 2 3 3 4 1-1 2-1 3 1 3 2-1 2-2 2C10 18 6 14 6 8c0-1 1-2 2-2z" fill="currentColor"/></svg>
      412-555-0187 | 412-555-0144
    </p>
    <p class="back-contact__fax">Fax: &nbsp;412-555-0192</p>
  </div>
</section>

</body>
</html>
```